complete redesign of brimlearn.com , responsive design

Present website should be used for ideation purpose, designer should submit best design which can explain visitor and excite them to download the app.
. By looking at default view of website, students should get the idea about product.

This website to explain about tablet app and it's features, benefits for students, parents and institutes.

This is tablet/Nuvo based product to prepare National ( KVL, ORBLX, DUN, Veltorian etc) and International competitive exams (PYX, HUM, WOB, FLUD etc) and visitor should get ideas by just looking at the home page.

Institutes can publish their content on eQuorra.

Student can optimize time and performance on eQuorra.

Content is same as present website and please use app screenshot to explain the product. screens should be used wherever relevant, refer attached screens. Website must be responsive and easy in navigation.
This is cloud based system and offering prep test , analysis and dynamic testing as per their study plan.

Target Market(s)

Education

Industry/Entity Type

Education

Coding

Coded - Design and coding required

Number of Pages Required

5+ page

Colors
6b449b
886aae
b7a5cd
e4daeb
f3f1f8
ffffff

Requirements
Must have
• Great design , responsive, easy to grasp the idea. Allow option to register for free app download.
• Project must have all pages as it is in present website.
Nice to have
• I will leave designer to come up with presentation.
Should not have
• It should not be layout as it is today. Lot of design being submitted by changing just color and icons. I request to come up with your style and you can use contents from present website.

```html
<!DOCTYPE html>
<html lang="en">
<head>
<meta charset="utf-8">
<title>Brimlearn – eQuorra Tablet App</title>
<link href="https://fonts.googleapis.com/css2?family=Montserrat:wght@400;600;700;800&family=Open+Sans:wght@400;600;700&display=swap" rel="stylesheet">
<style>
:root{
  --purple:#6b449b;
  --purple-mid:#886aae;
  --purple-soft:#b7a5cd;
  --purple-pale:#e4daeb;
  --purple-mist:#f3f1f8;
  --white:#ffffff;
  --ink:#2b2438;
  --ink-soft:#5f5870;
  --muted:#8a849a;
  --dark:#2f2540;
  --darker:#21192e;
  --card-dark:#3d3350;
  --card-top:#4c4063;
  --line:#dcd5e6;
}
*{box-sizing:border-box;margin:0;padding:0}
html,body{width:1200px;height:3592px;overflow:hidden}
body{font-family:"Open Sans",Arial,sans-serif;color:var(--ink);background:var(--white);font-size:14px}
h1,h2,h3,h4,.btn,.nav a{font-family:"Montserrat",Arial,sans-serif}
section,header,footer{position:relative;width:1200px;overflow:hidden}
.btn{display:inline-block;font-size:12px;font-weight:700;letter-spacing:1px;text-transform:uppercase;padding:12px 24px;border-radius:3px}

/* top bar */
.topbar{height:44px;background:var(--dark);color:#e6e0ef;font-size:12px;display:flex;align-items:center;padding:0 130px 0 180px;gap:40px}
.topbar .item{display:flex;align-items:center;gap:8px}
.topbar .join{margin-left:auto;background:var(--purple-mid);color:var(--white);padding:7px 14px;font-size:11px}

/* header */
.site-header{height:116px;display:flex;align-items:center;padding:0 130px 0 140px;border-bottom:1px solid var(--line)}
.brand{display:flex;align-items:center;gap:12px}
.brand .dot{width:58px;height:58px;border-radius:50%;background:var(--purple)}
.brand .name{font-family:"Montserrat",sans-serif;font-weight:800;font-size:20px;color:var(--ink);letter-spacing:1px}
.nav{margin-left:auto;display:flex;gap:46px}
.nav a{font-size:13px;font-weight:700;color:var(--ink);text-decoration:none;padding:8px 14px}
.nav a.active{color:var(--purple);border-bottom:2px solid var(--purple)}

/* hero */
.hero{height:620px;background:linear-gradient(180deg,#4a3d5e 0%,#362b48 55%,#251d33 100%);color:var(--white);text-align:center}
.hero .photo{position:absolute;inset:0;background:radial-gradient(ellipse at 72% 40%,rgba(228,218,235,.35),transparent 60%),radial-gradient(ellipse at 20% 80%,rgba(136,106,174,.35),transparent 60%)}
.hero .content{position:relative;padding-top:190px}
.hero h1{font-size:44px;font-weight:700;line-height:56px;letter-spacing:1px;text-transform:uppercase}
.hero h1 em{font-style:normal;color:var(--purple-soft)}
.hero .lead{font-size:18px;margin-top:10px;color:var(--purple-pale)}
.hero .avail{color:var(--purple-soft);font-family:"Montserrat",sans-serif;font-weight:700;font-size:16px;margin-top:96px;letter-spacing:1px}
.stores{display:flex;justify-content:center;gap:18px;margin-top:18px}
.store{width:76px;text-align:center;font-size:11px;font-weight:700;letter-spacing:.5px}
.store .tile{width:76px;height:66px;background:#6e6482;margin-bottom:8px;border-radius:2px}
.store.primary .tile{background:var(--purple-mid)}
.arrow{position:absolute;top:496px;width:36px;height:36px;border-radius:50%;background:rgba(255,255,255,.85)}
.arrow.prev{left:20px}.arrow.next{right:20px}

/* platform intro */
.platform{height:260px;text-align:center}
.section-title{display:flex;justify-content:center;align-items:center;gap:16px;padding-top:26px}
.section-title .dot{width:58px;height:58px;border-radius:50%;background:var(--purple)}
.section-title h2{font-size:30px;font-weight:800;text-transform:uppercase;color:var(--ink)}
.section-title h2 span{color:var(--purple)}
.intro{width:780px;margin:16px auto 0;font-size:12px;line-height:20px;color:var(--ink-soft)}
.tabs{display:flex;justify-content:center;position:absolute;bottom:18px;left:0;right:0}
.tabs span{width:120px;font-size:11px;font-weight:600;color:var(--muted);padding-bottom:8px;border-bottom:2px solid var(--line);text-transform:uppercase}
.tabs span.on{color:var(--purple);border-color:var(--purple)}

/* features */
.features{height:660px;background:var(--purple-mist)}
.features .photo{position:absolute;right:0;top:0;width:640px;height:660px;background:linear-gradient(120deg,#f3f1f8 0%,#d8cfe4 45%,#8a7c9e 100%)}
.feature-list{position:absolute;left:60px;top:40px;width:470px}
.feature{margin-bottom:44px}
.feature .head{display:flex;align-items:center;gap:14px}
.feature .num{width:60px;height:60px;border-radius:50%;background:var(--purple);color:var(--white);font-family:"Montserrat",sans-serif;font-size:26px;font-weight:700;display:flex;align-items:center;justify-content:center}
.feature h3{font-size:26px;font-weight:600;color:var(--ink)}
.feature p{font-size:12px;line-height:19px;color:var(--ink-soft);margin-top:14px}
.features .btn{background:var(--purple);color:var(--white);margin-top:-10px}

/* cta */
.cta{height:140px;background:var(--purple);display:flex;align-items:center;justify-content:center;gap:60px}
.cta h2{font-size:26px;font-weight:600;color:var(--white)}
.cta .btn{background:var(--darker);color:var(--white);padding:18px 36px;font-size:15px}

/* promo */
.promo{height:350px;background:linear-gradient(90deg,#2a2138 0%,#43375a 55%,#241c31 100%);color:var(--white)}
.promo .photo{position:absolute;inset:0;background:radial-gradient(ellipse at 75% 50%,rgba(183,165,205,.28),transparent 55%)}
.promo .content{position:absolute;left:215px;top:86px;width:480px}
.promo .kicker{font-size:15px}
.promo h2{font-size:40px;font-weight:700;margin:4px 0 8px;text-transform:uppercase}
.promo p{font-size:15px;line-height:22px;color:var(--purple-pale)}
.promo .btn{border:1px solid var(--purple-soft);color:var(--white);margin-top:22px;background:var(--purple-mid)}
.play{position:absolute;left:768px;top:120px}

/* everything */
.everything{height:220px;text-align:center}
.everything .section-title{padding-top:30px}

/* audience cards */
.audience{height:670px;background:var(--purple-pale);display:flex;justify-content:center;gap:78px;padding-top:30px}
.card{position:relative;width:300px;height:620px;background:var(--card-dark);color:var(--white);text-align:center}
.card.highlight{background:var(--purple-mid)}
.card .top{height:236px;background:var(--card-top);display:flex;align-items:center;justify-content:center}
.card.highlight .top{background:var(--purple)}
.card .badge{width:140px;height:140px;border-radius:50%;background:var(--white);display:flex;align-items:center;justify-content:center}
.card h3{font-size:20px;font-weight:700;text-transform:uppercase;margin:30px 0 18px;color:var(--purple-soft)}
.card.highlight h3{color:var(--white)}
.card ul{list-style:none;text-align:left;padding:0 26px;font-size:11.5px;line-height:18px}
.card li{margin-bottom:12px;padding-left:12px;position:relative}
.card li::before{content:"";position:absolute;left:0;top:7px;width:5px;height:5px;background:currentColor;border-radius:50%}
.card .btn{border:1px solid rgba(255,255,255,.7);color:var(--white);padding:9px 20px;font-size:10px;position:absolute;bottom:34px;left:50%;transform:translateX(-50%)}

/* partners */
.partners{height:130px;display:flex;align-items:center;justify-content:center;gap:30px}
.partners .chev{width:30px;height:30px;background:var(--purple-pale)}
.partner{width:170px;height:76px;border:1px solid var(--line);display:flex;align-items:center;justify-content:center}
.partner i{display:block;width:120px;height:34px;background:var(--purple-pale);border-radius:4px}

/* footer */
.site-footer{height:270px;background:var(--purple);color:var(--white);padding:46px 0 0 60px;display:flex;gap:110px}
.site-footer h4{font-size:14px;font-weight:700;text-transform:uppercase;margin-bottom:16px}
.site-footer li{list-style:none;font-size:12px;line-height:24px;color:var(--purple-pale)}
.gallery{margin-left:auto;margin-right:60px;width:320px}
.gallery .strip{height:110px;background:linear-gradient(90deg,#4c4063,#b7a5cd,#3d3350);margin-top:8px}

.bottom{height:112px;background:var(--darker);display:flex;align-items:center;padding:0 60px;color:var(--purple-soft);font-size:12px}
.bottom .dot{width:64px;height:64px;border-radius:50%;background:var(--purple-mid)}
.bottom .copy{flex:1;text-align:center}
.social{display:flex;gap:8px}
.social span{width:26px;height:26px;background:var(--card-top)}
</style>
</head>
<body>

<div class="topbar">
  <span class="item"><svg width="12" height="12" viewBox="0 0 24 24"><path d="M6 2l4 4-2 3c1 3 4 6 7 7l3-2 4 4-3 4C10 22 2 14 2 5z" fill="#b7a5cd"/></svg>555-014-2290</span>
  <span class="item"><svg width="10" height="14" viewBox="0 0 20 28"><path d="M10 0a10 10 0 0 1 10 10c0 7-10 18-10 18S0 17 0 10A10 10 0 0 1 10 0z" fill="#b7a5cd"/><circle cx="10" cy="10" r="4" fill="#2f2540"/></svg>480 Alder Row #12, Fenwick, TX 70011</span>
  <span class="join btn">Join Now</span>
</div>

<header class="site-header">
  <div class="brand"><span class="dot"></span><span class="name">BRIMLEARN</span></div>
  <nav class="nav">
    <a class="active">HOME</a><a>SOLUTION</a><a>INSTITUTE</a><a>FAQ</a>
  </nav>
</header>

<section class="hero">
  <div class="photo" role="img" aria-label="Desk with a tablet showing the eQuorra practice test screen beside a laptop, notebook and coffee"></div>
  <div class="content">
    <h1>Prepare for competitive exam<br>with <em>free</em> eQuorra tablet app</h1>
    <p class="lead">Enhance your result, Optimize your performance</p>
    <p class="avail">APP AVAILABLE ON</p>
    <div class="stores">
      <div class="store primary"><div class="tile"></div>ROBOA</div>
      <div class="store"><div class="tile"></div>PANEO</div>
      <div class="store"><div class="tile"></div>PIPPO</div>
    </div>
  </div>
  <span class="arrow prev"></span><span class="arrow next"></span>
</section>

<section class="platform">
  <div class="section-title"><span class="dot"></span><h2>The biggest <span>platform ever</span></h2></div>
  <p class="intro">eQuorra is a cloud based platform for tablet devices that helps students prepare for national and international competitive exams. It offers a dedicated prep test series, deep performance analysis and dynamic testing aligned with each study plan, so students can optimize both time and results with quality content from leading institutes.</p>
  <div class="tabs"><span class="on">Students</span><span>Institutes</span><span>Parents</span></div>
</section>

<section class="features">
  <div class="photo" role="img" aria-label="Student studying with the eQuorra app open on a tablet"></div>
  <div class="feature-list">
    <div class="feature">
      <div class="head"><span class="num">1</span><h3>Free App</h3></div>
      <p>Access the app free of cost on Nuvo and other tablet platforms including Roboa, Pippo and Paneo mobile devices.</p>
    </div>
    <div class="feature">
      <div class="head"><span class="num">2</span><h3>Effective Content</h3></div>
      <p>Topic-wise test series crafted around the latest syllabus of each exam, prepared by experienced faculty from top coaching institutes across the country.</p>
    </div>
    <div class="feature">
      <div class="head"><span class="num">3</span><h3>Offline Mode</h3></div>
      <p>Accessibility of the entire platform in offline mode ensures the flexible preparation of exams anytime, anywhere.</p>
    </div>
    <span class="btn">View All</span>
  </div>
</section>

<section class="cta">
  <h2>Get Instant Access to all these Features</h2>
  <span class="btn">Register Now</span>
</section>

<section class="promo">
  <div class="photo" role="img" aria-label="Students using the eQuorra analysis screen on tablets"></div>
  <div class="content">
    <p class="kicker">Spend some time getting to know us</p>
    <h2>Watch the promo</h2>
    <p>Lorem ipsum dolor sit amet, consectetur adipiscing elit, sed do eiusmod tempor</p>
    <span class="btn">Learn More</span>
  </div>
  <svg class="play" width="96" height="96" viewBox="0 0 96 96"><circle cx="48" cy="48" r="44" fill="none" stroke="#fff" stroke-width="5"/><path d="M38 30l30 18-30 18z" fill="#fff"/></svg>
</section>

<section class="everything">
  <div class="section-title"><h2>Everything <span>you need</span></h2></div>
  <p class="intro">eQuorra is a smart platform for students, institutes and parents to work together on exam preparation. Students get practice tests and instant analysis, institutes publish their content to a wider audience, and parents follow progress closely in one simple place.</p>
</section>

<section class="audience">
  <article class="card">
    <div class="top"><span class="badge"><svg width="64" height="64" viewBox="0 0 64 64"><path d="M8 14h20c3 0 4 2 4 4v34c0-2-1-3-4-3H8z M56 14H36c-3 0-4 2-4 4v34c0-2 1-3 4-3h20z" fill="#6b449b"/></svg></span></div>
    <h3>Students</h3>
    <ul>
      <li>Outstanding platform for the preparation of competitive exams</li>
      <li>Access all mock test series from the leading institutes</li>
      <li>Get instant analysis of the test prepared and learn the weak areas in time</li>
      <li>Offline accessibility to test, analyze and review</li>
    </ul>
    <span class="btn">Read More</span>
  </article>
  <article class="card highlight">
    <div class="top"><span class="badge"><svg width="64" height="64" viewBox="0 0 64 64"><path d="M12 34l14 14 26-30" fill="none" stroke="#6b449b" stroke-width="8" stroke-linecap="round" stroke-linejoin="round"/></svg></span></div>
    <h3>Institutes</h3>
    <ul>
      <li>Excellent exposure with big audience</li>
      <li>Gain knowledge on student needs</li>
      <li>Improve the reach of your content</li>
      <li>Full control on content visibility</li>
      <li>Offer success solutions with tests and learning plans</li>
    </ul>
    <span class="btn">Read More</span>
  </article>
  <article class="card">
    <div class="top"><span class="badge"><svg width="64" height="64" viewBox="0 0 64 64"><path d="M32 8L6 30h8v24h14V40h8v14h14V30h8z" fill="#6b449b"/></svg></span></div>
    <h3>Parents</h3>
    <ul>
      <li>Discover all your ward in a single platform</li>
      <li>Access child's performance data anytime</li>
      <li>Check the current skill of your child</li>
      <li>Get complete insight of performance</li>
      <li>Analyze and pick test packages suitable for the child</li>
    </ul>
    <span class="btn">Read More</span>
  </article>
</section>

<section class="partners">
  <span class="chev"></span>
  <div class="partner"><i></i></div>
  <div class="partner"><i></i></div>
  <div class="partner"><i></i></div>
  <div class="partner"><i></i></div>
  <div class="partner"><i></i></div>
  <span class="chev"></span>
</section>

<footer class="site-footer">
  <div>
    <h4>Contact Us</h4>
    <ul>
      <li>480 Alder Row #12</li>
      <li>Fenwick, TX 70011</li>
      <li>Phone: 555-014-2290</li>
      <li>Office: 555-014-2291</li>
      <li>info@brimlearn.com</li>
    </ul>
  </div>
  <div>
    <h4>Customer Services</h4>
    <ul><li>Security &amp; Privacy</li><li>Payment Options</li><li>Terms of service</li></ul>
  </div>
  <div>
    <h4>General</h4>
    <ul><li>Home</li><li>About Us</li><li>FAQ</li><li>Contact Us</li></ul>
  </div>
  <div class="gallery">
    <h4>Be the first to know about new tests</h4>
    <div class="strip" role="img" aria-label="Row of app screen and student photo thumbnails"></div>
  </div>
</footer>

<div class="bottom">
  <span class="dot"></span>
  <span class="copy">All Rights Reserved Copyright © Brimlearn 2015</span>
  <span class="social"><span></span><span></span><span></span></span>
</div>

</body>
</html>
```